Brighten-The-Room - DL Flyer - Kitchen Renovations & Cabinetry - Eye Catching Design

Please design a creative, professional DL flyer for us (DL Size: 98 x 210mmm), incorporating details outlined below...

Font: Helvetica Neue (same as logo)

Front: Main logo (01.eps) as a feature, website on the bottom (brighten-the-room.com.au).

Back: Three key words to be featured: Kitchens I Benchtops I Custom Cabinetry
2-3 clear images showing our work (more have been provided so you can select the images that work the best with the design). We have also attached the icon from our logo on 4 x different colour backgrounds, which could be incorporated (on back).
Text to include: 'Servicing all areas, we come to you!'

Contact details: 'Call us now on 0417 268 391'. enquiries@brighten-the-room.com.au Lic. No. BLD 738402

Look forward to seeing what you come up with.

Target Market(s)

Home owners, 35-80+ age bracket

Industry/Entity Type

Kitchen

Font styles to use
Other font styles liked:
• Helvetica Neue

Requirements
Must have
• Logo and website on front page of flyer. Minimum of 2-3 images incorporated. Contact details as per project description. Text on back page, 3 key words: Kitchens I Benchtops I Custom Cabinetry
• Creative, eye-catching design layout. Consistent theming with business card (see attached), including colours (grey, white, blues)
Nice to have
• Creative, eye-catching way to incorporate photos.
Should not have
• Not too busy/cluttered

```html
<!DOCTYPE html>
<html lang="en">
<head>
<meta charset="utf-8">
<title>Brighten-The-Room – DL Flyer</title>
<link rel="stylesheet" href="https://fonts.googleapis.com/css2?family=Arimo:wght@400;700&family=Open+Sans:wght@400;700&display=swap">
<style>
  :root {
    --page-bg: #f4f4f4;
    --charcoal: #5d5e60;
    --steel: #b3b4b6;
    --brand-blue: #4a8fd0;
    --heading-blue: #4a8fd4;
    --tagline-grey: #8a8b8d;
    --light-band: #efefef;
    --white: #ffffff;
  }
  * { box-sizing: border-box; margin: 0; padding: 0; }
  html, body {
    width: 1118px; height: 1200px; overflow: hidden;
    background: var(--page-bg);
  }
  .canvas { position: relative; width: 1118px; height: 1200px; }

  .flyer {
    position: absolute; width: 826px; height: 386px; overflow: hidden;
    background: var(--white);
  }
  .flyer--front { left: 87px; top: 220px; }
  .flyer--back  { left: 152px; top: 660px; background: var(--charcoal); }

  /* Front */
  .front__top-band { position: absolute; left: 0; top: 0; width: 100%; height: 16px; background: var(--steel); }
  .front__photo {
    position: absolute; left: 0; top: 16px; width: 100%; height: 321px;
    background: linear-gradient(180deg, #f6f6f4 0%, #fafafa 45%, #f1efe9 80%, #f7f6f3 100%);
  }
  .front__brand {
    position: absolute; left: 0; top: 150px; width: 100%; text-align: center;
    font-family: "Arimo", Helvetica, Arial, sans-serif;
  }
  .brand-name {
    font-size: 50px; font-weight: 700; letter-spacing: 1px;
    color: var(--charcoal); text-transform: uppercase; line-height: 1;
  }
  .brand-tagline {
    margin-top: 14px; font-size: 19px; font-weight: 400;
    letter-spacing: 6.2px; color: var(--tagline-grey); text-transform: uppercase;
  }
  .front__accent { position: absolute; left: 0; top: 337px; width: 100%; height: 5px; background: var(--brand-blue); }
  .front__footer {
    position: absolute; left: 0; top: 342px; width: 100%; height: 44px;
    background: var(--charcoal); color: var(--white);
    font-family: "Arimo", Helvetica, Arial, sans-serif; font-size: 21px;
    display: flex; align-items: center; justify-content: center;
  }

  /* Back */
  .back__header {
    position: absolute; left: 0; top: 0; width: 100%; height: 98px;
    display: flex; align-items: center; justify-content: center;
    font-family: "Arimo", Helvetica, Arial, sans-serif; font-size: 24px;
    color: var(--heading-blue); text-transform: uppercase;
  }
  .back__gallery {
    position: absolute; left: 0; top: 98px; width: 100%; height: 184px;
    background: var(--light-band);
  }
  .gallery__photo { position: absolute; top: 15px; height: 155px; }
  .gallery__photo--bathroom { left: 0; width: 271px; background: linear-gradient(135deg, #e9c6b4 0%, #f2e2d8 50%, #2f8a8a 100%); }
  .gallery__photo--benchtop { left: 277px; width: 272px; background: linear-gradient(180deg, #e8e8e6 0%, #cfcfcd 55%, #9a9b99 100%); }
  .gallery__photo--study    { left: 554px; width: 272px; background: linear-gradient(135deg, #d7c98c 0%, #f1e6a8 45%, #6e6d5c 100%); }
  .back__footer {
    position: absolute; left: 0; top: 282px; width: 100%; height: 104px;
    color: var(--white); text-align: center;
    font-family: "Open Sans", Helvetica, Arial, sans-serif;
  }
  .back__slogan { margin-top: 24px; font-size: 20px; text-transform: uppercase; }
  .back__contact { margin-top: 12px; font-size: 15px; }
  .back__contact strong { font-weight: 700; }
</style>
</head>
<body>
<main class="canvas">
  <section class="flyer flyer--front" aria-label="Flyer front">
    <div class="front__top-band"></div>
    <div class="front__photo" role="img" aria-label="Faded photo of a bright white kitchen with sink and benchtop"></div>
    <div class="front__brand">
      <div class="brand-name">Brighten-The-Room</div>
      <div class="brand-tagline">Cabinetry solutions for your home</div>
    </div>
    <div class="front__accent"></div>
    <div class="front__footer">www.brighten-the-room.com.au</div>
  </section>

  <section class="flyer flyer--back" aria-label="Flyer back">
    <h2 class="back__header">Kitchens | Benchtops | Custom Cabinetry</h2>
    <div class="back__gallery">
      <div class="gallery__photo gallery__photo--bathroom" role="img" aria-label="Bathroom vanity with teal towels"></div>
      <div class="gallery__photo gallery__photo--benchtop" role="img" aria-label="Stone benchtop with cooktop and kettle"></div>
      <div class="gallery__photo gallery__photo--study" role="img" aria-label="Custom study desk with shelving and plant"></div>
    </div>
    <div class="back__footer">
      <p class="back__slogan">Servicing all areas, we come to you!</p>
      <p class="back__contact">Call us now on <strong>0417 268 391</strong> | enquiries@brighten-the-room.com.au | Lic. No. BLD 738402</p>
    </div>
  </section>
</main>
</body>
</html>
```